PREMIUM Pagewall Page Design - A+++ Designers Wanted

** DO NOT ATTEMPT TO CONTACT ME THROUGH SEARCHING ON SEEKRA OR EMAILING ME THROUGH MY WEBSITE **

I need an amazing, fresh, contemporary Pagewall banner design created, using supplied photos.

You must be able to excellent graphics deisgn and photoshop skills to 'manipulate' photos to extend them / modify them for working on a horizontal banner.

Target Market(s)

Agency, Advertising Agency, Creative, Designers, Social Media, Online

Industry/Entity Type

Seekra

Font styles to use
Serif
Sans Serif

Requirements
Must have
• It must be fresh, clean, uncluttered and bold, and have text in the same font style (Arial Bold).
• Here are the photos you can download to choose from https://www.filecrate-share.example/sh/47kkwpt219qmzav/BCDnYPT1z6L5Fhyk8j1FcNcJb?dl=0
• For Text Style Sample : You can use any combination of Yellow, Black, White and Blue as per "SAMPLE UPLOAD FILE 1".
• Text : Pagewall Text must say "MAKING CENTURY OLD STORY TELLING A BRAND NEW EXPERIENCE" (see www.pagewall.example/fastlakeow for example)
• Second Project - To be awarded to winner of Pagewall project and paid additional $$
• Blurtix Text: I am open to designs and styles here. You can try any combination of "OWEN FASTLAKE" logo (see attached) and words like "GLOBAL FUTURIST" "STORY TELLER". I will leave you to design some ideas.
• The image must also be viewable on mobile & desktop, without losing any text.
• The 'profile' headshot photo for both can also be changed to suit your design.
Nice to have
• Must have a premium, fresh and uncluttered look. You should explore how to get the most out of the photos, and can edit them to create / extend the image to make it fit the banner space.
Should not have
• No funny or silly standard / off the shelf designs
• ** DO NOT ATTEMPT TO CONTACT ME THROUGH SEARCHING ON SEEKRA OR EMAILING ME THROUGH MY WEBSITE **

```html
<!DOCTYPE html>
<html lang="en">
<head>
<meta charset="UTF-8">
<title>Story Telling Banner</title>
<link rel="stylesheet" href="https://fonts.googleapis.com/css2?family=Nunito+Sans:wght@400;800&display=swap">
<style>
  :root {
    --bg-dark: #232323;
    --bg-mid: #2f2f2f;
    --accent-yellow: #f5b800;
    --rule-olive: #b9b24a;
    --text-white: #ffffff;
    --portrait-top: #3b3f86;
    --portrait-bottom: #1d2550;
  }
  * { margin: 0; padding: 0; box-sizing: border-box; }
  html, body {
    width: 1200px;
    height: 457px;
    overflow: hidden;
    background: var(--bg-dark);
  }
  .banner {
    position: relative;
    width: 1200px;
    height: 457px;
    overflow: hidden;
    background: var(--bg-mid);
    font-family: "Nunito Sans", Arial, sans-serif;
  }
  .banner__backdrop {
    position: absolute;
    inset: 0;
    width: 100%;
    height: 100%;
  }
  .rule {
    position: absolute;
    height: 1px;
    background: var(--rule-olive);
  }
  .rule--top { left: 587px; top: 111px; width: 229px; }
  .rule--bottom { left: 202px; top: 232px; width: 229px; }
  .headline {
    position: absolute;
    left: 0;
    top: 0;
    text-transform: uppercase;
    line-height: 1;
    white-space: nowrap;
  }
  .headline__lead,
  .headline__main {
    position: absolute;
    display: block;
  }
  .headline__lead {
    left: 205px;
    top: 127px;
    color: var(--accent-yellow);
    font-weight: 400;
    font-size: 32.5px;
    letter-spacing: 0;
  }
  .headline__main {
    left: 202px;
    top: 181px;
    color: var(--text-white);
    font-weight: 800;
    font-size: 31px;
    letter-spacing: 0.3px;
  }
  .portrait {
    position: absolute;
    left: 728px;
    top: 12px;
    width: 364px;
    height: 445px;
  }
</style>
</head>
<body>
  <main class="banner">
    <svg class="banner__backdrop" viewBox="0 0 1200 457" preserveAspectRatio="none" aria-hidden="true">
      <defs>
        <radialGradient id="glowTop" cx="0.4" cy="0.05" r="0.7">
          <stop offset="0" stop-color="#3c3c3c"/>
          <stop offset="1" stop-color="#262626"/>
        </radialGradient>
        <linearGradient id="swoosh" x1="0" y1="0" x2="1" y2="1">
          <stop offset="0" stop-color="#3a3a3a" stop-opacity="0.9"/>
          <stop offset="1" stop-color="#2a2a2a" stop-opacity="0"/>
        </linearGradient>
      </defs>
      <rect width="1200" height="457" fill="url(#glowTop)"/>
      <path d="M0 190 C 250 170, 520 270, 720 457 L 0 457 Z" fill="#252525"/>
      <path d="M320 230 C 500 245, 640 340, 730 457 L 700 457 C 610 350, 480 260, 320 230 Z" fill="url(#swoosh)"/>
      <path d="M600 0 C 800 60, 1000 40, 1200 120 L 1200 0 Z" fill="#333333" opacity="0.6"/>
    </svg>

    <div class="rule rule--top"></div>
    <h1 class="headline">
      <span class="headline__lead">Making Century Old Story Telling</span>
      <span class="headline__main">A Brand New Experience</span>
    </h1>
    <div class="rule rule--bottom"></div>

    <svg class="portrait" viewBox="0 0 364 445" role="img" aria-label="Portrait photo of a man in a navy zip jacket, lit with blue light">
      <defs>
        <linearGradient id="portraitFill" x1="0" y1="0" x2="0" y2="1">
          <stop offset="0" stop-color="var(--portrait-top)"/>
          <stop offset="1" stop-color="var(--portrait-bottom)"/>
        </linearGradient>
      </defs>
      <path d="M150 0 H 220 Q 242 0 242 30 V 150 L 250 168 Q 300 190 335 215 Q 352 240 356 300 L 364 445 H 0 L 12 300 Q 18 240 40 215 Q 90 185 130 168 L 128 150 V 30 Q 128 0 150 0 Z" fill="url(#portraitFill)"/>
    </svg>
  </main>
</body>
</html>
```